Business Card, Stationary with Shark Logo for Personal Injury Lawyer

I need business cards and stationery with a shark logo for my Personal Injury Law Practice. Has to have this written on it:
Martin K. Hollis
Injury Lawyer
The Corvell Building
718 Tandy Street
Providence, Rhode Island 02908
401-627-4193
Martinhollis.com

Contact Information for Business Card

Martin K. Hollis, Injury Lawyer, address, 401-627-4193, martinhollis.com

```html
<!DOCTYPE html>
<html lang="en">
<head>
<meta charset="utf-8">
<title>Martin K. Hollis – Business Card</title>
<link rel="stylesheet" href="https://fonts.googleapis.com/css2?family=Roboto:wght@400;500;700&display=swap">
<style>
  :root {
    --backdrop: #e6e8eb;
    --card: #f1f4f7;
    --navy: #25235f;
    --ink-soft: #5f6168;
  }
  * { margin: 0; padding: 0; box-sizing: border-box; }
  html, body {
    width: 1200px;
    height: 900px;
    overflow: hidden;
    background: var(--backdrop);
    font-family: "Roboto", sans-serif;
  }
  .card {
    position: absolute;
    left: 363px;
    width: 475px;
    height: 271px;
    background: var(--card);
  }
  .card--front { top: 145px; }
  .card--back { top: 484px; }

  .wordmark {
    position: absolute;
    left: 0;
    right: 0;
    top: 134px;
    transform: translateY(-50%);
    text-align: center;
    font-weight: 700;
    font-size: 32px;
    letter-spacing: 0.5px;
    color: var(--navy);
    text-transform: uppercase;
  }

  .identity {
    position: absolute;
    right: 250px;
    top: 118px;
    text-align: right;
  }
  .identity__name {
    font-weight: 500;
    font-size: 15.5px;
    color: var(--navy);
    text-transform: uppercase;
    line-height: 1.2;
  }
  .identity__role {
    font-size: 11px;
    color: var(--ink-soft);
    margin-top: 3px;
  }

  .divider {
    position: absolute;
    left: 237px;
    top: 95px;
    width: 1px;
    height: 81px;
    background: var(--navy);
  }

  .contact {
    position: absolute;
    left: 250px;
    top: 90px;
    font-size: 11px;
    color: var(--ink-soft);
    line-height: 15px;
  }
  .contact__address { margin-bottom: 12px; }
  .contact__line {
    display: flex;
    align-items: center;
    gap: 8px;
  }
  .contact__icon { width: 9px; height: 9px; fill: var(--navy); flex: none; }
</style>
</head>
<body>
  <section class="card card--front">
    <div class="wordmark">Martin K. Hollis</div>
  </section>

  <section class="card card--back">
    <div class="identity">
      <div class="identity__name">Martin K. Hollis</div>
      <div class="identity__role">Injury Lawyer</div>
    </div>
    <div class="divider"></div>
    <div class="contact">
      <div class="contact__address">
        The Corvell Building<br>
        718 Tandy Street<br>
        Providence, Rhode Island 02908
      </div>
      <div class="contact__line">
        <svg class="contact__icon" viewBox="0 0 24 24" aria-hidden="true">
          <path d="M6.6 10.8a15.1 15.1 0 0 0 6.6 6.6l2.2-2.2a1 1 0 0 1 1-.25 11.4 11.4 0 0 0 3.6.57 1 1 0 0 1 1 1V20a1 1 0 0 1-1 1A17 17 0 0 1 3 4a1 1 0 0 1 1-1h3.5a1 1 0 0 1 1 1c0 1.25.2 2.45.57 3.57a1 1 0 0 1-.25 1z"/>
        </svg>
        <span>401-627-4193</span>
      </div>
      <div class="contact__line">
        <svg class="contact__icon" viewBox="0 0 24 24" aria-hidden="true">
          <path d="M12 2a10 10 0 1 0 0 20 10 10 0 0 0 0-20zm6.9 6h-2.9a15.7 15.7 0 0 0-1.4-3.6A8 8 0 0 1 18.9 8zM12 4c.8 1.2 1.5 2.5 1.9 4h-3.8c.4-1.5 1.1-2.8 1.9-4zM4.3 14a8.2 8.2 0 0 1 0-4h3.4a16.5 16.5 0 0 0 0 4zm.8 2h2.9c.3 1.3.8 2.5 1.4 3.6A8 8 0 0 1 5.1 16zM8 8H5.1a8 8 0 0 1 4.3-3.6C8.8 5.5 8.3 6.7 8 8zm4 12c-.8-1.2-1.5-2.5-1.9-4h3.8c-.4 1.5-1.1 2.8-1.9 4zm2.3-6H9.7a14.7 14.7 0 0 1 0-4h4.6a14.7 14.7 0 0 1 0 4zm.3 5.6c.6-1.1 1.1-2.3 1.4-3.6h2.9a8 8 0 0 1-4.3 3.6zm1.7-5.6a16.5 16.5 0 0 0 0-4h3.4a8.2 8.2 0 0 1 0 4z"/>
        </svg>
        <span>Martinhollis.com</span>
      </div>
    </div>
  </section>
</body>
</html>
```